Business Card for Yachting Management Company

Need a business card design for a new yachting project management company. Attached is the logo for the company.
Our clients are large yacht owners and captains.
Design must be in the style of the logo. Modern, elegant.

Example of data to show:
Peter Hollis
Project Manager
(+34) 612 738 104
peter@quorvane.net
Quorvane Management - Meridel Tower, Office 22 - KRB - Palma de Mallorca

The data above will have to be changed (by me) for the different people in the company over the next years.

Will be printed using PrintNova (Lustre Card Series). They provide these guidelines for the size:
"the actual size of the card is 1050 x 600 pixels. However, the full bleed size is 1083 x 633 pixels, and the safe printing area is 1008 x 558 pixels."

```html
<!DOCTYPE html>
<html lang="en">
<head>
<meta charset="utf-8">
<title>Quorvane Management – Business Card</title>
<link rel="stylesheet" href="https://fonts.googleapis.com/css2?family=Roboto:wght@400;500;700&display=swap">
<style>
  :root {
    --backdrop: #aaaaaa;
    --card: #252525;
    --card-back: #282828;
    --facet: #464646;
    --brand-blue: #1873c2;
    --text-white: #ffffff;
    --text-grey: #9b9b9b;
  }
  html, body {
    margin: 0;
    padding: 0;
    width: 1200px;
    height: 1000px;
    overflow: hidden;
    background: var(--backdrop);
    font-family: "Roboto", Arial, sans-serif;
  }
  .canvas {
    position: relative;
    width: 1200px;
    height: 1000px;
  }
  .card {
    position: absolute;
    width: 514px;
    height: 296px;
    overflow: hidden;
    box-shadow: 0 18px 40px rgba(0,0,0,0.28);
  }
  .card--front {
    left: 343px;
    top: 152px;
    background: var(--card);
  }
  .card--back {
    left: 341px;
    top: 517px;
    background: var(--card-back);
  }
  .front-facet {
    position: absolute;
    inset: 0;
  }
  .contact {
    position: absolute;
    left: 70px;
    top: 63px;
    font-size: 16px;
    line-height: 19.5px;
    color: var(--text-grey);
  }
  .contact p { margin: 0; }
  .contact__name {
    color: var(--brand-blue);
    font-weight: 700;
    font-size: 17px;
  }
  .contact__role {
    color: var(--text-white);
    font-size: 17.5px;
    margin-bottom: 20px !important;
  }
  .contact__lines { margin-bottom: 18px !important; }
  .company-name {
    position: absolute;
    right: 20px;
    text-align: right;
    color: var(--brand-blue);
    font-weight: 700;
    font-size: 14px;
    line-height: 16px;
    letter-spacing: 0.5px;
    margin: 0;
  }
  .card--front .company-name { bottom: 14px; }
  .back-texture {
    position: absolute;
    left: 18px;
    top: 10px;
    width: 480px;
    height: 276px;
    background: linear-gradient(100deg, #3a3a3a 0%, #303030 45%, #1c1c1c 100%);
  }
  .card--back .company-name { bottom: 14px; }
</style>
</head>
<body>
<div class="canvas">
  <section class="card card--front">
    <svg class="front-facet" width="514" height="296" viewBox="0 0 514 296" aria-hidden="true">
      <polygon points="295,296 514,0 514,296" fill="var(--facet)"/>
    </svg>
    <div class="contact">
      <p class="contact__name">Peter Hollis</p>
      <p class="contact__role">Project Manager</p>
      <p class="contact__lines">(+34) 612 738 104<br>peter@quorvane.net</p>
      <p>Meridel Tower,<br>Office 22 - KRB<br>Palma de Mallorca</p>
    </div>
    <p class="company-name">Quorvane<br>Management</p>
  </section>

  <section class="card card--back">
    <div class="back-texture" role="img" aria-label="Tonal repeating brand pattern fading from grey to black"></div>
    <p class="company-name">Quorvane<br>Management</p>
  </section>
</div>
</body>
</html>
```